Modern Lawfirm Business Card Design

We're looking for a business card to incorporate the newly created logo we had made.

Ideally looking for a law firm business card demonstrating, modern, minimalist, strong/bold design.

I'm open to any design honestly, but nothing "flashy".

Target Market(s)

Immigration law, family immigration, humanitarian, general legal

Industry/Entity Type

Law Firm

Contact Information for Business Card

Please use dummy information, name, street address, city, state, phone number, email, website.

Font styles to use
Serif
Sans Serif

Requirements
Must have
• Please use dummy information, name, street address, city, state, phone number, email, website.

```html
<!DOCTYPE html>
<html lang="en">
<head>
<meta charset="utf-8">
<title>Calder Immigration Law – Business Cards</title>
<link rel="stylesheet" href="https://fonts.googleapis.com/css2?family=Cinzel:wght@400;700&family=Open+Sans:wght@400;600&display=swap">
<style>
  :root {
    --brand-blue: #1f64a8;
    --brand-blue-dark: #17528d;
    --ink-grey: #555b61;
    --rule-grey: #8a8f94;
    --card-white: #f7f7f6;
    --page-bg: #e9e7e3;
  }
  * { box-sizing: border-box; margin: 0; padding: 0; }
  html, body { width: 1200px; height: 1023px; overflow: hidden; }
  body {
    background: var(--page-bg);
    position: relative;
    font-family: "Open Sans", Arial, sans-serif;
  }
  .card {
    position: absolute;
    width: 580px;
    height: 331px;
    border-radius: 3px;
    box-shadow: 0 10px 28px rgba(0,0,0,0.18);
  }
  /* Front */
  .card-front {
    left: 70px; top: 80px;
    background: var(--card-white);
    border-bottom: 10px solid var(--brand-blue);
  }
  .wordmark {
    position: absolute;
    display: flex; align-items: center; gap: 12px;
    font-family: "Cinzel", Georgia, serif;
    font-weight: 700;
    color: var(--brand-blue);
  }
  .card-front .wordmark { left: 40px; top: 58px; font-size: 30px; letter-spacing: 1px; }
  .wordmark-square { width: 18px; height: 18px; background: var(--brand-blue); flex: none; }
  .front-rule {
    position: absolute; left: 235px; right: 40px; top: 170px;
    border-top: 1.5px solid var(--rule-grey);
  }
  .person { position: absolute; left: 40px; top: 150px; }
  .person-name { color: var(--brand-blue); font-weight: 600; font-size: 20px; line-height: 1.2; }
  .person-role { color: var(--ink-grey); font-size: 15px; }
  .address {
    position: absolute; left: 40px; bottom: 30px;
    color: var(--ink-grey); font-size: 14px; line-height: 1.45;
  }
  .contacts {
    position: absolute; right: 40px; bottom: 30px;
    list-style: none; text-align: right;
    color: var(--ink-grey); font-size: 14px; line-height: 1.6;
  }
  .contacts li { display: flex; align-items: center; justify-content: flex-end; gap: 8px; }
  .contacts .web { color: var(--brand-blue); }
  .contacts svg { width: 13px; height: 13px; fill: var(--brand-blue); }
  /* Back */
  .card-back {
    left: 550px; top: 600px;
    background: linear-gradient(160deg, var(--brand-blue), var(--brand-blue-dark));
  }
  .card-back .wordmark {
    left: 0; right: 0; top: 120px; justify-content: center;
    color: #ffffff; font-size: 38px; letter-spacing: 2px;
  }
  .card-back .wordmark-square { background: #ffffff; width: 22px; height: 22px; }
  .back-url {
    position: absolute; left: 0; right: 0; bottom: 60px; text-align: center;
    color: #dbe7f3; font-size: 14px; letter-spacing: 4px;
  }
</style>
</head>
<body>
  <section class="card card-front" aria-label="Business card front">
    <div class="wordmark"><span class="wordmark-square"></span>Calder Immigration Law</div>
    <div class="person">
      <p class="person-name">Daniel Reyes</p>
      <p class="person-role">Founder</p>
    </div>
    <div class="front-rule"></div>
    <p class="address">210 Harbor Street, Suite 4<br>Portland, OR 97201</p>
    <ul class="contacts">
      <li>+555 014 2290
        <svg viewBox="0 0 24 24"><path d="M6.6 10.8a15 15 0 0 0 6.6 6.6l2.2-2.2c.3-.3.7-.4 1-.2 1.1.4 2.3.6 3.6.6.6 0 1 .4 1 1V20c0 .6-.4 1-1 1C10.6 21 3 13.4 3 4c0-.6.4-1 1-1h3.5c.6 0 1 .4 1 1 0 1.3.2 2.5.6 3.6.1.3 0 .7-.2 1z"/></svg></li>
      <li>info@calderlaw.com
        <svg viewBox="0 0 24 24"><path d="M2 5h20v14H2z M3 6l9 7 9-7" fill="none" stroke="currentColor"/><path d="M2 5h20v14H2zM4 7v10h16V7l-8 6z"/></svg></li>
      <li class="web">www.calderlaw.com
        <svg viewBox="0 0 24 24"><circle cx="12" cy="12" r="10"/></svg></li>
    </ul>
  </section>

  <section class="card card-back" aria-label="Business card back">
    <div class="wordmark"><span class="wordmark-square"></span>Calder Immigration Law</div>
    <p class="back-url">www.calderlaw.com</p>
  </section>
</body>
</html>
```